food company needs a design for tea biscuit packaging

we need a design for our tea biscuit
the design must include our logo and a file ready to go to print from the front and back
the size is 13 *4 cm
i've uploaded an example

Requirements
Must have
• the biscuit must have the same shape as the one i upload
Nice to have
• if you can include Arabic to the design that would be perfect

```html
<!DOCTYPE html>
<html lang="en">
<head>
<meta charset="utf-8">
<title>Velmora Tea Biscuit – Pack Layout 13 × 4 cm</title>
<link rel="stylesheet" href="https://fonts.googleapis.com/css2?family=Fraunces:opsz,wght@144,900&family=Roboto:wght@700&family=Nunito:wght@700;800&family=Source+Sans+3:wght@400&display=swap">
<style>
  :root {
    --brand-red: #ec2833;
    --paper: #ffffff;
    --ink: #111111;
    --placeholder-grey: #cccccc;
    --placeholder-text: #ffffff;
    --guide: #222222;
    --biscuit-light: #f1c777;
    --biscuit-deep: #d9993f;
  }
  * { box-sizing: border-box; margin: 0; padding: 0; }
  html, body { width: 1200px; height: 677px; overflow: hidden; background: var(--paper); }
  .sheet { position: relative; width: 1200px; height: 677px; font-family: "Source Sans 3", sans-serif; color: var(--ink); }

  /* dimension guides */
  .dim-line { position: absolute; border-color: var(--guide); border-style: solid; border-width: 0; }
  .dim-width { left: 281px; top: 54px; width: 872px; height: 18px; border-top-width: 1px; border-left-width: 1px; border-right-width: 1px; }
  .dim-height { left: 245px; width: 22px; border-left-width: 1px; border-top-width: 1px; }
  .dim-height.front { top: 85px; height: 268px; }
  .dim-height.back { top: 353px; height: 268px; border-bottom-width: 1px; }
  .dim-label { position: absolute; font-size: 26px; line-height: 1; }
  .dim-label.width { left: 740px; top: 18px; }
  .dim-label.front { left: 183px; top: 208px; }
  .dim-label.back { left: 182px; top: 477px; }
  .panel-label { position: absolute; font-size: 26px; line-height: 34px; }
  .panel-label.front { left: 69px; top: 186px; }
  .panel-label.back { left: 57px; top: 461px; }

  /* pack artwork */
  .pack { position: absolute; left: 281px; top: 85px; width: 872px; height: 536px; background: var(--paper); border: 1px solid var(--guide); overflow: hidden; }
  .band { position: absolute; top: 0; bottom: 0; background: var(--brand-red); }
  .band.left { left: 0; width: 188px; }
  .band.right { left: 680px; right: 0; }
  .fold-line { position: absolute; left: 0; right: 0; top: 268px; border-top: 1px solid var(--guide); }

  .biscuit-photo { position: absolute; border-radius: 14px; background: linear-gradient(135deg, var(--biscuit-light), var(--biscuit-deep)); box-shadow: 0 6px 18px rgba(0,0,0,.18); }
  .biscuit-photo.top-right { left: 542px; top: -10px; width: 303px; height: 112px; }
  .biscuit-photo.left { left: 30px; top: 144px; width: 306px; height: 192px; }
  .biscuit-photo.bottom-right { left: 536px; top: 445px; width: 306px; height: 110px; }

  .brand-name { position: absolute; font-family: "Roboto", sans-serif; font-weight: 700; color: var(--brand-red); font-size: 22px; letter-spacing: 1px; white-space: nowrap; line-height: 1; }
  .brand-name.front { left: 329px; top: 38px; }
  .brand-name.back { left: 656px; top: 322px; font-size: 20px; }

  .wordmark { position: absolute; left: 214px; top: 83px; width: 440px; text-align: center; font-family: "Fraunces", serif; font-weight: 900; font-size: 96px; line-height: 1; color: var(--ink); letter-spacing: -1px; white-space: nowrap; }

  .product-tag { position: absolute; background: var(--brand-red); color: var(--paper); font-family: "Roboto", sans-serif; font-weight: 700; border-radius: 20px 0 0 20px; display: flex; align-items: center; justify-content: center; white-space: nowrap; line-height: 1; }
  .product-tag.front { left: 458px; top: 190px; width: 222px; height: 39px; font-size: 29px; padding-left: 6px; }
  .product-tag.back { left: 606px; top: 366px; width: 206px; height: 39px; font-size: 29px; padding-left: 6px; }

  .info-panel { position: absolute; left: 61px; top: 289px; width: 754px; height: 222px; background: var(--paper); border: 3px solid var(--ink); }
  .placeholder { position: absolute; background: var(--placeholder-grey); color: var(--placeholder-text); font-family: "Nunito", sans-serif; font-weight: 800; display: flex; align-items: center; justify-content: center; text-align: center; }
  .placeholder.nutrition { left: 12px; top: 12px; width: 518px; height: 193px; font-size: 30px; }
  .placeholder.barcode { left: 545px; top: 126px; width: 194px; height: 79px; font-size: 30px; line-height: 32px; }
</style>
</head>
<body>
<main class="sheet">
  <div class="dim-line dim-width"></div>
  <span class="dim-label width">13cm</span>

  <div class="dim-line dim-height front"></div>
  <div class="dim-line dim-height back"></div>
  <span class="dim-label front">4 cm</span>
  <span class="dim-label back">4 cm</span>
  <p class="panel-label front">front<br>part</p>
  <p class="panel-label back">back<br>part</p>

  <section class="pack">
    <div class="band left"></div>
    <div class="band right"></div>

    <div class="biscuit-photo top-right" role="img" aria-label="Photo of a bitten embossed rectangular tea biscuit"></div>
    <div class="biscuit-photo bottom-right" role="img" aria-label="Photo of an embossed rectangular tea biscuit"></div>
    <div class="biscuit-photo left" role="img" aria-label="Photo of a bitten embossed rectangular tea biscuit"></div>

    <span class="brand-name front">VELMORA</span>
    <h1 class="wordmark">Velmora</h1>
    <div class="product-tag front">TEA BISCUIT</div>

    <div class="fold-line"></div>

    <div class="info-panel">
      <div class="placeholder nutrition">nutrition facts label goes here</div>
      <div class="placeholder barcode">bar code<br>goes here</div>
    </div>
    <span class="brand-name back">VELMORA</span>
    <div class="product-tag back">TEA BISCUIT</div>
  </section>
</main>
</body>
</html>
```